Health and Wellness. I am an energetic, but not over the top, Certified Personal Trainer and Nutriti

I need a flyer, 8.5 x 11, representing my company to be displayed in a Doctor's office that specializes in Pain Medicine. Most, if not all, of these clients experience pain or have some chronic diseases such as high blood pressure, high cholesterol, back pain, joint pain, etc. So the flyer should convey that exercise and nutrition reduce/relieves pain and references some of these ailments. Ideally, the flyer should depict an overweight person exercising with a content, or somewhat content or smiling expression on their face in some part of the flyer. My services cover nutrition and include personal training to where I Ideally train people in their home, equipment permitting, or outside in our local Floridian Parks, and sometimes beaches. This flyer will be in a display case, and the bottom right 8.5 x5 cm will need to be blank, or allow for me to input the back of my business car into it, as I'll have business cards readily available in front of the flyer to be taken. I've included some versions of my logos to be added to the flyer. The other picture is of the flyer holder, with business card area, that this flyer will be presented in. Finally, I've attached a pic of what the back of my business card looks like to be input into that bottom right hand corner. You'll be able to see the area in the bottom right that will display my business cards.
Target Market(s)
People looking for weight loss through Nutrition and Fitness. Those looking to relieve joint and/or back pain or those with Chronic diseases such as high blood pressure, high cholesterol, etc.
Industry/Entity Type
Doctor
Requirements
Must have
- Resemble my Logo's color scheme: Red, Teal, and Grey. Some type of photo of an overweight or slightly overweight person exercising.

```html
<!DOCTYPE html>
<html lang="en">
<head>
<meta charset="utf-8">
<title>Kessler's Fitness – Flyer</title>
<link rel="stylesheet" href="https://fonts.googleapis.com/css2?family=Asap+Condensed:wght@500&family=Open+Sans:ital,wght@0,400;1,700&display=swap">
<style>
  :root {
    --stage: #5f6062;
    --brand-red: #ed1c24;
    --headline-red: #e8434a;
    --panel-grey: #808285;
    --name-grey: #a7a8aa;
    --white: #ffffff;
    --social-blue: #3aa0e0;
  }
  * { box-sizing: border-box; margin: 0; padding: 0; }
  html, body { width: 1037px; height: 1200px; overflow: hidden; background: var(--stage); }
  .flyer {
    position: absolute; left: 151px; top: 122px; width: 749px; height: 969px;
    box-shadow: 0 4px 14px rgba(0,0,0,.45); overflow: hidden;
  }
  .flyer-art { position: absolute; inset: 0; width: 100%; height: 100%; }
  .brand {
    position: absolute; left: 18px; top: 72px; width: 230px; text-align: center;
    font-family: "Asap Condensed", sans-serif; font-weight: 500;
    font-size: 26px; color: var(--name-grey);
  }
  .headline {
    position: absolute; left: 0; top: 528px; width: 453px; text-align: center;
    font-family: "Asap Condensed", sans-serif; font-weight: 500;
    font-size: 47px; line-height: 63px; color: var(--headline-red); letter-spacing: -0.5px;
  }
  .pitch {
    position: absolute; left: 454px; top: 522px; width: 295px; text-align: center;
    font-family: "Asap Condensed", sans-serif; font-weight: 500;
    font-size: 19px; line-height: 23px; color: var(--white);
  }
  .pitch p + p { margin-top: 24px; }
  .card {
    position: absolute; left: 514px; top: 663px; width: 174px; height: 298px;
    background: linear-gradient(160deg, #2b2b2d, #111112);
    font-family: "Open Sans", sans-serif; color: var(--white); text-align: center;
    padding-top: 22px;
  }
  .card-title { font-style: italic; font-weight: 700; color: var(--brand-red); font-size: 15px; margin-bottom: 4px; }
  .card-list { list-style: none; font-size: 11.5px; line-height: 17px; }
  .card-owner { font-size: 11.5px; margin-top: 22px; }
  .card-contact { font-size: 10.5px; line-height: 17px; margin-top: 20px; }
  .card-handle { font-size: 10.5px; margin-top: 20px; color: #cfcfcf; }
  .card-social { display: flex; justify-content: center; gap: 12px; margin-top: 6px; }
  .card-social span { width: 21px; height: 21px; border-radius: 50%; background: var(--social-blue); }
</style>
</head>
<body>
<main class="flyer">
  <svg class="flyer-art" viewBox="0 0 850 1100" preserveAspectRatio="none">
    <defs>
      <linearGradient id="darkTexture" x1="0" y1="0" x2="1" y2="1">
        <stop offset="0" stop-color="#3a3b3e"/>
        <stop offset=".5" stop-color="#1d1d1f"/>
        <stop offset="1" stop-color="#2b2c2e"/>
      </linearGradient>
      <linearGradient id="gymPhoto" x1="0" y1="0" x2="1" y2="0">
        <stop offset="0" stop-color="#d6dadf"/>
        <stop offset=".45" stop-color="#c9a9ae"/>
        <stop offset=".7" stop-color="#d99aa6"/>
        <stop offset="1" stop-color="#b9bec5"/>
      </linearGradient>
      <linearGradient id="parkPhoto" x1="0" y1="0" x2="0" y2="1">
        <stop offset="0" stop-color="#a9b7a5"/>
        <stop offset=".6" stop-color="#6f8a5c"/>
        <stop offset="1" stop-color="#7d7160"/>
      </linearGradient>
    </defs>
    <rect class="backdrop" width="850" height="1100" fill="url(#darkTexture)"/>
    <rect class="content-white" x="0" y="470" width="515" height="515" fill="#ffffff"/>
    <rect class="side-panel" x="515" y="420" width="335" height="545" fill="#808285"/>
    <path class="hero-photo" role="img" aria-label="Photo of a smiling woman in a pink tank top doing a push-up in a gym"
          d="M0,300 C200,175 500,65 850,12 L850,420 C700,470 600,492 500,495 C300,498 120,470 0,440 Z" fill="url(#gymPhoto)"/>
    <path class="hero-swoosh" d="M0,290 C200,160 500,50 850,0 L850,14 C500,66 200,178 0,312 Z" fill="#e4e4e4"/>
    <path class="hero-edge-white" d="M0,440 C120,470 300,498 500,495 L580,492 L580,505 C350,515 150,495 0,462 Z" fill="#f2f2f2"/>
    <path class="hero-band-red" d="M0,462 C150,495 350,515 580,505 L580,540 C350,555 150,545 0,525 Z" fill="#ed1c24"/>
    <path class="side-stripe" d="M790,434 L850,406 L850,418 L796,444 Z" fill="#ed1c24"/>
    <circle cx="690" cy="444" r="122" fill="#ffffff"/>
    <circle class="trainer-photo" role="img" aria-label="Photo of the trainer exercising on a park bench under oak trees" cx="690" cy="444" r="116" fill="url(#parkPhoto)"/>
    <path class="footer-dark" d="M0,965 C200,1000 400,1010 583,1000 L583,1100 L0,1100 Z" fill="url(#darkTexture)"/>
    <path class="footer-swoosh" d="M0,965 C200,1000 400,1010 583,998 L583,1004 C400,1018 200,1010 0,980 Z" fill="#e4e4e4"/>
    <path class="footer-line-red" d="M180,997 C300,1008 450,1010 583,1000 L583,1010 C450,1016 300,1014 180,1003 Z" fill="#ed1c24"/>
    <path class="footer-right-dark" d="M583,985 L850,950 L850,1100 L583,1100 Z" fill="url(#darkTexture)"/>
    <path class="footer-right-red" d="M583,988 C700,975 790,962 850,930 L850,950 C790,972 700,988 583,1000 Z" fill="#ed1c24"/>
  </svg>

  <header class="brand">Kessler's Fitness</header>

  <h1 class="headline">Do you suffer from<br>chronic joint or back pain,<br>high blood pressure<br>or high cholesterol?</h1>

  <div class="pitch">
    <p>A personalized fitness and nutrition<br>plan can change your life.</p>
    <p>Let Kessler's Fitness<br>show you how.</p>
  </div>

  <aside class="card">
    <p class="card-title">Personal Training</p>
    <ul class="card-list">
      <li>-Online-</li>
      <li>-In Your Home-</li>
      <li>-Parks and Beaches-</li>
      <li>-Bride, Groom, Bridal Party-</li>
    </ul>
    <p class="card-owner">Ryan Kessler Owner/Trainer</p>
    <p class="card-contact">555-014-2288<br>kesslersfitness1@example.com<br>www.kesslersfitness.com</p>
    <p class="card-handle">@kesslersfitness</p>
    <div class="card-social"><span></span><span></span><span></span><span></span></div>
  </aside>
</main>
</body>
</html>
```